5'x15' banner for sustainable apartments

Meadow 457 is a sustainable community that focuses on well being of tenants and reduction of carbon footprint.
Need an eye catching banner to be displayed on the side of a building. Walls are gray (see pic), so it's a perfect canvass to splash some colors. Banner shall include the word "apartments" and represent sustainability (ie. sustainable apartments).
Please check website to see more about the community: www.meadow457.example
Dimensions are 5' W x 15' H.
Daily traffic is approx. 20k cars.

Target Market(s)

we target environmentally conscious tenants who want to live in a community of like-minded people. We have a community garden, and reuse "gray" water for irrigation. We've also implemented recycling programs.
We've also built a deck were we have yoga practices -free of charge- for our tenants and guests.

Industry/Entity Type

Community

Font styles to use
Other font styles liked:
• Leelawadee UI

Requirements
Must have
• Should be understood that these are apartments for rent.
• whatever imagery is to be used, should have a strong association with sustainability.
• If any text, use Leelawadee UI font.
Nice to have
• well being imagery / association
• The picture with the painted mural is not from the subject building, but liked the drawing, so could spark some idea.

```html
<!DOCTYPE html>
<html lang="en">
<head>
<meta charset="utf-8">
<title>Meadow 457 – Sustainable Apartments Banner</title>
<link rel="stylesheet" href="https://fonts.googleapis.com/css2?family=Open+Sans:wdth,wght@75..100,500..800&display=swap">
<style>
  :root {
    --backdrop: #4f6787;
    --banner-white: #ffffff;
    --ink: #2a2c2c;
    --accent-red: #b3262e;
    --band-dark: #222a27;
    --band-text: #ffffff;
    --art-tone: #dfe3e1;
  }
  * { margin: 0; padding: 0; box-sizing: border-box; }
  html, body {
    width: 1200px;
    height: 960px;
    overflow: hidden;
    background: var(--backdrop);
  }
  .canvas {
    position: relative;
    width: 1200px;
    height: 960px;
    background: var(--backdrop);
  }
  .banner {
    position: absolute;
    left: 466px;
    top: 80px;
    width: 267px;
    height: 800px;
    background: var(--banner-white);
    font-family: "Open Sans", Arial, sans-serif;
    font-stretch: 85%;
  }
  .headline {
    position: absolute;
    top: 72px;
    left: 0;
    width: 100%;
    text-align: center;
    color: var(--ink);
    font-weight: 700;
    text-transform: uppercase;
  }
  .headline .line-small {
    display: block;
    font-size: 32px;
    line-height: 33px;
    letter-spacing: -0.5px;
  }
  .headline .line-big {
    display: block;
    font-size: 72px;
    line-height: 56px;
    font-weight: 800;
    color: var(--accent-red);
    letter-spacing: -1px;
  }
  .headline .lead { margin-bottom: 6px; }
  .headline .tail { margin-top: 8px; }
  .skyline-art {
    position: absolute;
    left: 28px;
    top: 388px;
    width: 206px;
    height: 215px;
    background: linear-gradient(180deg, #f2f4f3 0%, var(--art-tone) 100%);
  }
  .brand-band {
    position: absolute;
    left: 0;
    bottom: 0;
    width: 100%;
    height: 197px;
    background: var(--band-dark);
    color: var(--band-text);
  }
  .brand-name {
    position: absolute;
    left: 42px;
    top: 26px;
    width: 196px;
    font-weight: 800;
    font-size: 46px;
    line-height: 50px;
    letter-spacing: 0;
    text-transform: uppercase;
  }
  .brand-name .word { display: block; text-align: center; }
  .brand-name .number { display: block; text-align: right; }
  .call-line {
    position: absolute;
    left: 0;
    bottom: 28px;
    width: 100%;
    text-align: center;
    font-weight: 600;
    font-size: 22px;
  }
</style>
</head>
<body>
  <main class="canvas">
    <section class="banner">
      <h1 class="headline">
        <span class="line-small">Sustainable</span>
        <span class="line-small lead">Apartments</span>
        <span class="line-big">Just</span>
        <span class="line-big">Steps</span>
        <span class="line-small tail">From</span>
        <span class="line-small">Linden</span>
        <span class="line-small">District.</span>
      </h1>
      <div class="skyline-art" role="img" aria-label="Outline illustration of two apartment towers with window grids"></div>
      <footer class="brand-band">
        <p class="brand-name"><span class="word">Meadow</span><span class="number">457</span></p>
        <p class="call-line">Call: 555-014-2938</p>
      </footer>
    </section>
  </main>
</body>
</html>
```